Non-Fiction Book On Creativity - Cover Design / Physical and E-Book

I am looking for designs for my first book! It's called: Stillness Makes Harvest. The subtitle is: 27 Notes On Tending Gardens, Mending Fences, And Keeping A Patient Home.
It's a series of short lessons and principals on creativity and it will be a Kindle book and a physical book.
I'm really open to any type of designs but have attached some screenshots of other book covers that have a design and style that I like.
Please let me know if you have any questions or need any more information.
Creativity / Self-Help / Personal Development

```html
<!DOCTYPE html>
<html lang="en">
<head>
<meta charset="utf-8">
<title>Stillness Makes Harvest — Cover Wrap</title>
<link href="https://fonts.googleapis.com/css2?family=Dosis:wght@400;500;600&display=swap" rel="stylesheet">
<style>
  :root {
    --page: #ffffff;
    --paper: #e6dbcf;
    --navy: #1c3566;
    --pink: #e5468f;
    --teal: #1aa5a5;
    --green: #2aad4f;
    --steel: #4a86a0;
    --olive: #a8c13a;
    --orange: #e8a04e;
    --purple: #6a3fa0;
    --mint: #2fc4a0;
    --splash-blue: #3db7d6;
    --splash-yellow: #e9e26a;
    --splash-red: #ec6a6a;
  }
  * { margin: 0; padding: 0; box-sizing: border-box; }
  html, body { width: 1200px; height: 1200px; overflow: hidden; background: var(--page); }
  body { position: relative; font-family: "Dosis", sans-serif; color: var(--navy); }

  .wrap { position: absolute; left: 0; top: 166px; width: 1200px; height: 868px; background: var(--paper); }

  /* back cover */
  .back-birds {
    position: absolute; left: 144px; top: 50px; width: 260px; height: 84px;
    background: radial-gradient(ellipse at 80% 60%, rgba(106,63,160,.55), transparent 60%),
                radial-gradient(ellipse at 40% 50%, rgba(26,165,165,.35), transparent 65%);
  }
  .blurb {
    position: absolute; left: 63px; top: 146px; width: 438px;
    font-size: 16px; line-height: 31.2px; text-align: justify; font-weight: 400;
    hyphens: auto;
  }
  .blurb .lead { font-size: 30px; font-weight: 500; }
  .back-splash {
    position: absolute; left: 0; top: 578px; width: 560px; height: 290px;
    background:
      radial-gradient(ellipse at 15% 75%, rgba(236,106,106,.55), transparent 45%),
      radial-gradient(ellipse at 35% 60%, rgba(233,226,106,.6), transparent 45%),
      radial-gradient(ellipse at 30% 85%, rgba(61,183,214,.5), transparent 40%),
      radial-gradient(ellipse at 60% 55%, rgba(229,70,143,.35), transparent 40%),
      radial-gradient(ellipse at 10% 40%, rgba(42,173,79,.3), transparent 40%);
  }
  .barcode-space { position: absolute; left: 358px; top: 718px; width: 186px; height: 114px; background: #fff; }

  /* spine */
  .spine { position: absolute; left: 566px; top: 0; width: 66px; height: 868px; background: var(--navy); }
  .spine-title, .spine-author {
    position: absolute; left: 0; width: 66px; writing-mode: vertical-rl;
    display: flex; align-items: center; color: var(--paper); font-weight: 500;
  }
  .spine-title { top: 30px; font-size: 27px; letter-spacing: 0.5px; }
  .spine-author { top: 526px; font-size: 22px; letter-spacing: 15px; }

  /* front cover */
  .title {
    position: absolute; left: 632px; top: 24px; width: 568px; text-align: center;
    font-size: 92px; line-height: 80px; font-weight: 500; letter-spacing: 2px; text-transform: uppercase;
  }
  .title .line { display: block; }
  .subtitle {
    position: absolute; left: 632px; top: 270px; width: 568px; text-align: center;
    font-size: 25px; line-height: 28px; font-weight: 600; letter-spacing: -0.3px;
  }
  .front-art {
    position: absolute; left: 636px; top: 320px; width: 564px; height: 474px;
    background:
      radial-gradient(ellipse at 32% 62%, rgba(28,53,102,.55), transparent 38%),
      radial-gradient(ellipse at 52% 60%, rgba(229,70,143,.45), transparent 35%),
      radial-gradient(ellipse at 50% 45%, rgba(26,165,165,.45), transparent 38%),
      radial-gradient(ellipse at 75% 35%, rgba(233,226,106,.55), transparent 40%),
      radial-gradient(ellipse at 80% 55%, rgba(236,106,106,.4), transparent 35%),
      radial-gradient(ellipse at 92% 18%, rgba(61,183,214,.4), transparent 30%);
  }
  .author {
    position: absolute; left: 632px; top: 812px; width: 568px; text-align: center;
    font-size: 29px; font-weight: 500; letter-spacing: 19px; text-indent: 19px;
  }

  .c-navy { color: var(--navy); } .c-pink { color: var(--pink); } .c-teal { color: var(--teal); }
  .c-green { color: var(--green); } .c-steel { color: var(--steel); } .c-olive { color: var(--olive); }
  .c-orange { color: var(--orange); } .c-purple { color: var(--purple); } .c-mint { color: var(--mint); }
</style>
</head>
<body>
  <div class="wrap">
    <section class="back-cover">
      <div class="back-birds" role="img" aria-label="Flock of small watercolour birds in flight"></div>
      <p class="blurb"><span class="lead">Lorem ipsum</span> dolor sit amet, consectetur adipiscing elit, sed do eiusmod tempor incididunt ut labore et dolore magna aliqua. Ut enim ad minim veniam, quis nostrud exercitation ullamco laboris nisi ut aliquip ex ea commodo consequat. Duis aute irure dolor in reprehenderit in voluptate velit esse cillum dolore eu fugiat nulla pariatur. Excepteur sint occaecat cupidatat non proident, sunt in culpa qui officia deserunt mollit anim id est laborum.<br>Lorem ipsum dolor sit amet, consectetur adipiscing elit, sed do eiusmod tempor incididunt ut labore et dolore magna aliqua. Ut enim ad minim veniam, quis nostrud exercitation ullamco laboris nisi ut aliquip ex ea commodo consequat. Duis aute irure dolor in reprehenderit in voluptate velit esse cillum dolore eu fugiat nulla pariatur.</p>
      <div class="back-splash" role="img" aria-label="Multicoloured watercolour paint splatter"></div>
      <div class="barcode-space"></div>
    </section>

    <section class="spine">
      <div class="spine-title"><span><span class="c-pink">S</span><span class="c-teal">T</span><span class="c-green">I</span><span class="c-steel">L</span><span class="c-olive">L</span><span class="c-orange">N</span><span class="c-purple">E</span><span class="c-mint">S</span><span class="c-teal">S</span> MAKES HARVEST</span></div>
      <div class="spine-author">AUTHOR NAME</div>
    </section>

    <section class="front-cover">
      <h1 class="title">
        <span class="line"><span class="c-navy">S</span><span class="c-pink">T</span><span class="c-teal">I</span><span class="c-green">L</span><span class="c-steel">L</span><span class="c-olive">N</span><span class="c-orange">E</span><span class="c-purple">S</span><span class="c-mint">S</span></span>
        <span class="line">Makes</span>
        <span class="line">Harvest</span>
      </h1>
      <p class="subtitle">27 Notes On Tending Gardens, Mending Fences,<br>And Keeping A Patient Home</p>
      <div class="front-art" role="img" aria-label="Swirling line-drawn brain turning into colourful paint splatter with birds flying off"></div>
      <p class="author">AUTHOR NAME</p>
    </section>
  </div>
</body>
</html>
```